CHIP BAG AND LOGO DESIGN - A salty snack that is focused on taste and texture

I need a logo and label design for our new brand "Vexamba". A salty snack that brings corn tortilla with extreme spices to excite the taste. First Flavor will be 'Trueno Pimienta and Kiwi'. Looking for a label design and a logo design for the Brand 'Vexamba'. This brand will have multiple types of snacks and all with different flavors and heat levels.

Target Market(s)

10- 25 year old

Industry/Entity Type

Salty Snacks

Font styles to use
Sans Serif
Other font styles liked:
• Arial, Bauhaus 93, Berlin Sans FB Demi, Cooper Black

Colors
59FF00
82FF00
B8FF75
E3FFCB
F4FFEA
FFF300
FFF600
FEFA6F
FFFEC7
FFFEE8
FFC000
F8CF3A
FAE287
FDF2CF
FEFAEE
F0912C
F2A743
F7CA91
FBE8D2
FDF5EE
EE7325
F08F49
F5BC92
FAE3D3
FDF4ED
EB3D1F
EC4F4E
F09395
F8D3D4
FCEDEE

Requirements
Must have
• Colors and design that pops, need the bags to jump off the shelf in a sea of competitors. I gave an example of Walrus Flax, I appreciate the artwork and design they did to differentiate their brand from others and appeal to the 10-25 demographics.
Nice to have
• Abstract / Cartoon like characteristics that speak of a south of the border recipe and origin. I would like to have in subtle grey or black background design much like the Aztec calendar that fills the space on a bag and/or a variation of that kind of design. In the front I'd like a character (maybe a warrior) of the same fashion. The logo (also being designed - "VEXAMBA") carefully blended into the artwork. Bold, Loud, jumps off the shelf with bright colors and graphics.
Should not have
• bland, boring, blah colors and designs. Should be fun and loud.

```html
<!DOCTYPE html>
<html lang="en">
<head>
<meta charset="utf-8">
<title>Vexamba – Trueno Pimienta and Kiwi</title>
<link href="https://fonts.googleapis.com/css2?family=Fredoka:wght@600&family=Oswald:wght@500&display=swap" rel="stylesheet">
<style>
  :root {
    --backdrop: #efeedd;
    --bag-core: #fbb034;
    --bag-mid: #f59a2a;
    --bag-edge: #ea5a17;
    --ink-brown: #a8622c;
    --band-brown: #8f4f22;
    --band-light: #b06a30;
    --band-rule: #f2a743;
    --label-text: #f7ca91;
    --glyph-light: #d9c39a;
    --glyph-dark: #8a6a45;
  }
  html, body {
    margin: 0;
    width: 1113px;
    height: 1200px;
    overflow: hidden;
    background: var(--backdrop);
  }
  .bag-front {
    position: absolute;
    left: 156px;
    top: 40px;
    width: 800px;
    height: 1120px;
    background: radial-gradient(ellipse 60% 55% at 50% 45%, var(--bag-core) 0%, var(--bag-mid) 60%, var(--bag-edge) 100%);
    overflow: hidden;
  }
  .pattern-band {
    position: absolute;
    top: 0;
    height: 203px;
    background:
      linear-gradient(180deg,
        var(--band-brown) 0px, var(--band-brown) 22px,
        var(--band-rule) 22px, var(--band-rule) 26px,
        var(--band-light) 26px, var(--band-light) 110px,
        var(--band-rule) 110px, var(--band-rule) 114px,
        var(--band-brown) 114px, var(--band-brown) 196px,
        var(--band-rule) 196px, var(--band-rule) 203px);
    opacity: 0.9;
  }
  .pattern-band--left { left: 0; width: 258px; }
  .pattern-band--right { right: 0; width: 250px; }
  .brand-label {
    position: absolute;
    left: 305px;
    top: 97px;
    width: 195px;
    height: 106px;
    background: var(--band-light);
    display: flex;
    align-items: center;
    justify-content: center;
  }
  .brand-name {
    margin: 0;
    font-family: "Oswald", "Arial Narrow", sans-serif;
    font-weight: 500;
    font-size: 40px;
    letter-spacing: 1px;
    color: var(--label-text);
  }
  .flavor-name {
    position: absolute;
    left: 0;
    right: 0;
    top: 298px;
    margin: 0;
    text-align: center;
    font-family: "Fredoka", "Berlin Sans FB Demi", sans-serif;
    font-weight: 600;
    font-size: 132px;
    line-height: 146px;
    letter-spacing: -2px;
    color: var(--ink-brown);
  }
  .flavor-name span { display: block; }
  .warrior-glyph {
    position: absolute;
    left: 216px;
    top: 728px;
    width: 374px;
    height: 361px;
    border-radius: 28px;
    background: radial-gradient(circle at 60% 60%, var(--glyph-light) 0%, #c8a877 55%, var(--glyph-dark) 100%);
  }
</style>
</head>
<body>
  <main class="bag-front">
    <div class="pattern-band pattern-band--left" role="img" aria-label="Brown Aztec-style scroll and key-fret border pattern"></div>
    <div class="pattern-band pattern-band--right" role="img" aria-label="Brown Aztec-style scroll and key-fret border pattern"></div>
    <div class="brand-label">
      <p class="brand-name">VEXAMBA</p>
    </div>
    <h1 class="flavor-name">
      <span>Trueno</span>
      <span>Pimienta</span>
      <span>and Kiwi</span>
    </h1>
    <div class="warrior-glyph" role="img" aria-label="Stylised Mesoamerican stone glyph illustration of a warrior with a spiral motif"></div>
  </main>
</body>
</html>
```